Business Card Design with new logo

Dorian Pelleway 4172
E 118th St Casey, IL 62420
Cell: 217-555-0193
pellewayrestoration@mailvane.test

Classic Car Restoration Services Buy Sell Trade Consign

Dorian Pelleway 9698
Cell: 217-555-0193

```html
<!DOCTYPE html>
<html lang="en">
<head>
<meta charset="utf-8">
<title>Pelleway Restoration LLC – Business Card</title>
<link rel="stylesheet" href="https://fonts.googleapis.com/css2?family=Crimson+Text&family=Sansita:ital,wght@0,800;1,800&display=swap">
<style>
  :root {
    --page: #c3ced3;
    --card: #2b2f37;
    --card-edge: #1f2228;
    --card-mesh: #3a3f4a;
    --red: #e8232f;
    --red-dim: #7a1f27;
    --white: #f2f4f5;
    --heading-font: "Sansita", sans-serif;
    --body-font: "Crimson Text", serif;
  }
  * { margin: 0; padding: 0; box-sizing: border-box; }
  html, body { width: 1200px; height: 1200px; overflow: hidden; background: var(--page); }
  .canvas { position: relative; width: 1200px; height: 1200px; }

  .card {
    position: absolute; left: 252px; width: 696px; height: 402px;
    background: var(--card); overflow: hidden;
    box-shadow: 0 6px 14px rgba(0,0,0,0.35);
  }
  .card--front { top: 136px; }
  .card--back { top: 660px; }

  .texture {
    position: absolute; inset: 0;
    background: radial-gradient(ellipse at 50% 45%, var(--card-mesh) 0%, var(--card) 55%, var(--card-edge) 100%);
  }

  .stripe-band {
    position: absolute; width: 48px;
    background: linear-gradient(180deg, var(--red-dim), var(--red) 50%, var(--red-dim));
    opacity: 0.85;
  }
  .stripe-band--front-right { right: 2px; top: 0; height: 218px; }
  .stripe-band--front-left  { left: 2px; top: 188px; height: 214px; }
  .stripe-band--back-left   { left: 2px; top: 0; height: 218px; }
  .stripe-band--back-right  { right: 2px; top: 186px; height: 216px; }

  .brand-name {
    position: absolute; left: 70px; right: 70px; top: 128px; text-align: center;
    font-family: var(--heading-font); font-style: normal; font-weight: 800;
    font-size: 64px; color: var(--red); line-height: 1.05; letter-spacing: 1px;
  }

  .services-title {
    position: absolute; left: 56px; right: 0; top: 2px; text-align: center;
    font-family: var(--heading-font); font-style: italic; font-weight: 800;
    font-size: 40px; color: var(--white); white-space: nowrap;
  }
  .services-list {
    position: absolute; left: 0; right: 0; top: 56px; text-align: center;
    font-family: var(--heading-font); font-style: italic; font-weight: 800;
    font-size: 29px; color: var(--white); word-spacing: 2px;
  }

  .contact {
    position: absolute; left: 170px; display: flex; align-items: center; gap: 14px;
    font-family: var(--body-font); color: var(--white); font-size: 23px; line-height: 1.4;
  }
  .contact--address { top: 124px; }
  .contact--phone { top: 215px; font-size: 26px; letter-spacing: 1px; }
  .contact--email { top: 295px; font-size: 26px; }
  .icon { width: 40px; height: 40px; flex: none; }
  .icon circle { fill: var(--red); }
  .icon .glyph { fill: var(--white); }
  .icon .glyph-stroke { fill: none; stroke: var(--white); stroke-width: 2; }

  .mini-brand {
    position: absolute; left: 10px; bottom: 10px;
    font-family: var(--heading-font); font-style: normal; font-weight: 800;
    font-size: 14px; color: var(--red); line-height: 1.1;
  }
</style>
</head>
<body>
<main class="canvas">

  <section class="card card--front">
    <div class="texture" role="img" aria-label="Dark hexagon mesh texture"></div>
    <div class="stripe-band stripe-band--front-right" role="img" aria-label="Red chevron stripe pointing down"></div>
    <div class="stripe-band stripe-band--front-left" role="img" aria-label="Red chevron stripe pointing up"></div>
    <h1 class="brand-name">Pelleway<br>Restoration LLC</h1>
  </section>

  <section class="card card--back">
    <div class="texture" role="img" aria-label="Dark hexagon mesh texture"></div>
    <div class="stripe-band stripe-band--back-left" role="img" aria-label="Red chevron stripe pointing down"></div>
    <div class="stripe-band stripe-band--back-right" role="img" aria-label="Red chevron stripe pointing up"></div>

    <h2 class="services-title">Classic Car Restoration Services</h2>
    <p class="services-list">Buy ● Sell ● Trade ● Consign</p>

    <div class="contact contact--address">
      <svg class="icon" viewBox="0 0 40 40"><circle cx="20" cy="20" r="20"/>
        <path class="glyph" d="M20 9a7 7 0 0 0-7 7c0 5 7 14 7 14s7-9 7-14a7 7 0 0 0-7-7zm0 10a3 3 0 1 1 0-6 3 3 0 0 1 0 6z"/></svg>
      <p>Dorian Pelleway 4172<br>E 118th St Casey, IL 62420</p>
    </div>
    <div class="contact contact--phone">
      <svg class="icon" viewBox="0 0 40 40"><circle cx="20" cy="20" r="20"/>
        <rect class="glyph-stroke" x="14" y="9" width="12" height="22" rx="2"/>
        <rect class="glyph" x="18.5" y="25.5" width="3" height="3" rx="1.5"/></svg>
      <p>217-555-0193</p>
    </div>
    <div class="contact contact--email">
      <svg class="icon" viewBox="0 0 40 40"><circle cx="20" cy="20" r="20"/>
        <rect class="glyph" x="10" y="13" width="20" height="14" rx="1"/>
        <polyline points="10,13 20,21 30,13" fill="none" stroke="#e8232f" stroke-width="2"/></svg>
      <p>pellewayrestoration@mailvane.test</p>
    </div>

    <p class="mini-brand">Pelleway<br>Restoration LLC</p>
  </section>

</main>
</body>
</html>
```